Brantley Invites you to Celebrate 50 Years with them

Email invitation using the attached logo files- design may also need to be converted to stationary.

Date: Tuesday May 15 2018
Time: 11 am - 1 pm
Where: Oak Hollow 4817 Garnet Lane Pigeon Forge TN 37841

Example: Brantley cordially Invites you to a luncheon to Celebrate 50 years of business!

* Use the colors in the logo to tie the invitation together

Target Market(s)

Business associates, vendors and leaders in community

Industry/Entity Type

Hospitality

Requirements
Must have
• logo attached and information provided in brief
Nice to have
• also be able to use as stationary
Should not have
• any additional images to purchase

```html
<!DOCTYPE html>
<html lang="en">
<head>
<meta charset="utf-8">
<title>Brantley 50th Anniversary Luncheon Invitation</title>
<link href="https://fonts.googleapis.com/css2?family=Cinzel:wght@400;500&display=swap" rel="stylesheet">
<style>
  :root {
    --panel-grey: #a5a6a9;
    --panel-edge: #8e8f92;
    --paper-light: #f4f4f5;
    --paper-mid: #d3d4d6;
    --ornament: #dcdddf;
    --ink: #47484b;
    --accent-blue: #3f7cc1;
    --white: #ffffff;
  }
  * { margin: 0; padding: 0; box-sizing: border-box; }
  html, body { width: 927px; height: 1200px; overflow: hidden; }
  body { font-family: "Cinzel", "Times New Roman", serif; }

  .invitation {
    position: relative;
    width: 927px;
    height: 1200px;
    overflow: hidden;
    background: radial-gradient(circle at 470px 590px, var(--paper-light) 0, #e6e6e8 220px, var(--paper-mid) 600px);
  }

  .side-panel {
    position: absolute;
    left: 0; top: 0;
    width: 372px; height: 1200px;
    background: var(--panel-grey);
    box-shadow: 3px 0 4px rgba(0,0,0,0.18);
  }

  .side-panel__ornament {
    position: absolute;
    left: 0; top: 0;
  }

  .side-panel__greeting {
    position: absolute;
    left: 56px; top: 40px;
    color: var(--white);
    font-size: 54px;
    font-weight: 400;
    line-height: 62px;
    letter-spacing: 1px;
  }

  .headline {
    position: absolute;
    left: 426px; top: 296px;
    color: var(--ink);
  }
  .headline__lead { font-size: 56px; line-height: 60px; }
  .headline__sub { font-size: 36px; line-height: 50px; }
  .headline__big { font-size: 60px; line-height: 70px; margin-top: 4px; }

  .divider {
    position: absolute;
    left: 410px; top: 644px;
    width: 432px;
    border-top: 1px dotted #8a8b8e;
  }

  .details {
    position: absolute;
    left: 411px; top: 694px;
    color: var(--ink);
    font-size: 26px;
    line-height: 34px;
  }
  .details__row { display: flex; margin-bottom: 30px; }
  .details__label { width: 117px; color: var(--accent-blue); }

  .banner {
    position: absolute;
    left: 0; top: 1024px;
    width: 927px; height: 66px;
    background: var(--accent-blue);
  }
  .banner__text {
    position: absolute;
    left: 278px; top: 18px;
    color: var(--white);
    font-size: 23px;
    letter-spacing: 1px;
  }

  .badge {
    position: absolute;
    left: 56px; top: 960px;
    width: 184px; height: 184px;
    border-radius: 50%;
    background: var(--white);
    border: 5px solid #c9cacc;
    box-shadow: 0 3px 8px rgba(0,0,0,0.25);
    display: flex; align-items: center; justify-content: center;
  }
  .badge__name {
    color: var(--accent-blue);
    font-size: 26px;
    font-weight: 500;
  }
</style>
</head>
<body>
  <main class="invitation">
    <aside class="side-panel">
      <svg class="side-panel__ornament" width="372" height="1200" role="img" aria-label="Decorative lace mandala ornament, half shown at panel edge">
        <path d="M372 288 A310 310 0 0 0 372 908 Z" fill="var(--ornament)"/>
      </svg>
      <h1 class="side-panel__greeting">Brantley<br>cordially<br>invites<br>you...</h1>
    </aside>

    <section class="headline">
      <p class="headline__lead">Join Us</p>
      <p class="headline__sub">for a Luncheon</p>
      <p class="headline__sub">Celebrating Our</p>
      <p class="headline__big">50 years</p>
      <p class="headline__big">in Business!</p>
    </section>

    <div class="divider"></div>

    <section class="details">
      <div class="details__row"><span class="details__label">Date</span><span>Tuesday, May 15, 2018</span></div>
      <div class="details__row"><span class="details__label">Time</span><span>11 am - 1 pm</span></div>
      <div class="details__row"><span class="details__label">Where</span><span>Oak Hollow<br>4817 Garnet Lane<br>Pigeon Forge TN 37841</span></div>
    </section>

    <div class="banner">
      <p class="banner__text">We Look Forward to Celebrating with You!</p>
    </div>

    <div class="badge"><span class="badge__name">Brantley</span></div>
  </main>
</body>
</html>
```